Corporate Web Design

Hello Designers,
Thank you for wanting to participate in designing a web design.
First off let me introduce ourselves, we are a precious metals refinery that is base in the west coast. Our Name is Sterling Harbor Metals Refinery. Our sole goal for this website is simplicity yet cleanliness and elegance. We want to demonstrate the process and procedures of what we do and who we are.
The Lay out:
We want about 4-5 Tabs that will help guide our customers through our website with ease. Some ideas of what we want to call the tabs might be….
1. Home
- This tab will take them to the home page
2. Contact Us
- Our contact information
- Client contact form
- Some sort of membership form?
3. Pick-up Service
- This tab will explain how this process works and what it in tells.
- This page will also have a section for requirements.
- This pickup service will only be available for members and people that have a good account with us.
4. How it Works
- This page will explain who we are and how we work.
- I would like to somehow creatively show the process and the steps we take in melting their gold.
Effects:
An effect that I would want to see is a live precious metal stock price. This price will automatically update and post the most recent and current price on the market of what the gold, silver etc prices. Here is a link of a company that has something similar, http://qlvt-refining.example/ what I like about this spot price pop up, is that it follows them all over the page. I like that idea.
I would also like some sort of slide show that has videos and demonstrations of our company and business.
These are all Websites of our competitors that we like many ideas from.
http://www.bzkw.example/
What we like about this website is the tab that says “Request Pick-up” With a form that they have to fill out. We would want more than just a form; we would want some sort of membership application.
http://vexmetals.example/
What I like about this website is the slideshow. It’s very simple yet professional. This is something that I would like to incorporate into our website. I also like the live metal market price.
http://qlvt-refining.example/
This is another example of a website that has a live spot price of the gold market. I like how the gold price follows you around the page. I would like to see some of your ideas with this.
http://www.dunmetals.example/
This website is very clean and simple. I like the colors. I would like a little more character than what they have but I like the simplicity.
The colors we like are black, white, silver, gold, Royal Blue etc; basically anything that creates a clean atmosphere. These colors match our logo and also have a very elegant and professional perception to them. Please do not limit yourselves to only our suggestions
These are links to our Logo with all different colors.
https://files.example/s/k27m4p91rtz8vqa/LOGO_black_background.png
https://files.example/s/9wnb3x61hdq2lfe/LOGO_black.png
https://files.example/s/m8rc215jqpv4kzo/LOGO_transparent_background.png
https://files.example/s/t3fy804lwmn6bsu/LOGO_white_background.png
These are links to a brochure of our business that represents and shows the process of what we do and demonstrates who we are.
https://files.example/s/h6dv592kqcx1rwa/inside_1.pdf
https://files.example/s/p4gl736nybe9tcu/inside_2.pdf
Bottom line we want to see examples of ideas and layouts that you have for a website. Please upload them and We will comment back on them.

```html
<!DOCTYPE html>
<html lang="en">
<head>
<meta charset="utf-8">
<title>How it Works – Sterling Harbor Metals Refinery</title>
<link rel="stylesheet" href="https://fonts.googleapis.com/css2?family=Oswald:wght@400;500&family=PT+Serif&display=swap">
<style>
:root{
  --gold:#f7c325;
  --gold-dark:#e0a912;
  --ink:#2b2824;
  --panel:#2d2b29;
  --panel-2:#1d1c1b;
  --paper:#f4f4f4;
  --grey:#e6e6e6;
  --label:#f2bf2a;
  --muted:#8a8a8a;
}
*{box-sizing:border-box;margin:0;padding:0}
html,body{width:680px;height:1200px;overflow:hidden}
body{position:relative;background:linear-gradient(#e4e4e4,#f6f6f6 40%,#f4f4f4);font-family:"Oswald",sans-serif;color:var(--ink)}
.abs{position:absolute}

.site-header{left:0;top:0;width:680px;height:73px;background:linear-gradient(#fff,#f6f6f6);box-shadow:0 1px 2px rgba(0,0,0,.08)}
.brand{left:0;width:680px;top:24px;text-align:center;font-family:"Oswald",sans-serif;font-weight:400;font-size:22px;letter-spacing:1.5px;color:#8c8c8c;text-transform:uppercase}
.login{left:575px;top:43px;width:33px;height:15px;background:var(--panel);color:var(--gold);font-size:9px;line-height:15px;text-align:center;border-radius:3px}

.nav-btn{top:90px;height:20px;width:70px;font-size:8.5px;line-height:20px;text-align:center;border-radius:3px;background:linear-gradient(#fff,#dcdcdc);box-shadow:0 1px 2px rgba(0,0,0,.3);color:#222;font-family:Arial,sans-serif}
.nav-btn.active,.nav-btn.calc{background:linear-gradient(#ffd54a,#f3b51a);font-weight:bold}

.band-gold{left:0;width:680px;background:var(--gold)}
.step-label{left:240px;width:200px;height:50px}
.step-label span{position:absolute;left:0;top:0;width:100%;height:36px;line-height:36px;text-align:center;color:var(--label);font-size:13.5px;font-weight:500;text-transform:uppercase;white-space:nowrap}
.step-label span.tight{font-size:12px;letter-spacing:-.1px}

.photo{width:131px;height:85px;border:2px solid #fff;box-shadow:0 1px 3px rgba(0,0,0,.35)}
.num{width:24px;height:20px;background:var(--panel);color:var(--gold);font-size:12px;line-height:20px;text-align:center;border-radius:2px}
.caption{width:160px;text-align:center;font-size:11px;line-height:14px;font-weight:500;color:var(--ink)}
.caption.lead{font-size:13.5px;line-height:16px;width:160px}
.intro{left:250px;top:248px;width:180px;text-align:center;font-size:16.5px;line-height:18px;font-weight:500}

.footer{left:0;top:1097px;width:680px;height:49px;background:#1c1c1c}
.badge{top:1106px;width:30px;height:30px;border-radius:50%;border:1px solid #555}
.badge.wide{width:86px;border-radius:3px;height:26px;top:1108px}

.ticker-bg{left:0;top:1146px;width:680px;height:54px;background:var(--gold)}
.ticker{left:71px;top:1152px;width:538px;height:48px;background:linear-gradient(var(--panel),var(--panel-2));border-radius:4px 4px 0 0;font-family:"PT Serif",serif}
.t-label{top:8px;font-size:10px;color:var(--gold)}
.t-field{top:24px;height:15px;font-size:8px;line-height:15px;background:linear-gradient(#5a5754,#3b3937);color:#eee;border-radius:2px;text-align:center}
.t-field.change{background:var(--gold);color:#222}
</style>
</head>
<body>

<header class="site-header abs">
  <div class="brand abs">Sterling Harbor Metals Refinery</div>
  <div class="login abs">Login</div>
</header>

<nav>
  <div class="nav-btn abs" style="left:74px">Home</div>
  <div class="nav-btn abs" style="left:148px">Contact Us</div>
  <div class="nav-btn abs" style="left:221px">Pick-up Service</div>
  <div class="nav-btn abs active" style="left:294px">How it Works</div>
  <div class="nav-btn abs calc" style="left:513px;width:93px">Scrap Calculator</div>
</nav>

<section class="step-one">
  <div class="band-gold abs" style="top:192px;height:199px"></div>
  <div class="step-label abs" style="top:153px">
    <svg width="200" height="50"><polygon points="2,0 198,0 194,36 6,36" fill="#2d2b29"/><polygon points="84,36 116,36 100,50" fill="#f4f4f4"/><polygon points="90,36 110,36 100,44" fill="#2d2b29"/></svg>
    <span>Step One – Verification</span>
  </div>
  <div class="photo abs" role="img" aria-label="Refinery building exterior" style="left:89px;top:227px;background:linear-gradient(#9ec7ea,#6f8a80 60%,#8a8a7a)"></div>
  <div class="caption lead abs" style="left:74px;top:322px">First you will bring your metals to our State of the Art and Secure Facility</div>
  <div class="intro abs">In this building we have a transaction window where we will weight your metals.</div>
  <div class="photo abs" role="img" aria-label="Staff member at the transaction window" style="left:459px;top:227px;background:linear-gradient(135deg,#d9d2c8,#8fa8b4 60%,#b99c8a)"></div>
  <div class="caption lead abs" style="left:444px;top:322px">We will then take your metals and store them in a safe while your metals wait to be melted.</div>
</section>

<section class="step-two">
  <div class="step-label abs" style="top:385px">
    <svg width="200" height="50"><polygon points="2,0 198,0 194,36 6,36" fill="#2d2b29"/><polygon points="90,36 110,36 100,44" fill="#2d2b29"/></svg>
    <span>Step Two – Melting</span>
  </div>

  <div class="photo abs" role="img" aria-label="Sorting scrap jewellery" style="left:89px;top:455px;background:linear-gradient(135deg,#3a3630,#a38a4a 55%,#2b2925)"></div>
  <div class="num abs" style="left:186px;top:527px">1</div>
  <div class="caption abs" style="left:74px;top:556px">We first sort through your metals to make sure that everything is prepared and ready for the melt.</div>

  <div class="photo abs" role="img" aria-label="Metals poured into the crucible" style="left:275px;top:455px;background:radial-gradient(circle at 50% 75%,#f07a22,#7a3a1c 40%,#3a3633 70%)"></div>
  <div class="num abs" style="left:372px;top:527px">2</div>
  <div class="caption abs" style="left:260px;top:556px">After prepping the metals, we then pour the metals into the crucible. Which is heated up to over 1900 degrees.</div>

  <div class="photo abs" role="img" aria-label="Stirring molten metal" style="left:459px;top:455px;background:radial-gradient(circle at 45% 80%,#f08a2a,#8a5a3a 40%,#6e6a66 75%)"></div>
  <div class="num abs" style="left:556px;top:527px">3</div>
  <div class="caption abs" style="left:444px;top:556px">We then commence to stir and mix the metals. This is to make sure the metals are completely homogenized.</div>

  <div class="photo abs" role="img" aria-label="Pouring metal into a mold" style="left:89px;top:631px;background:radial-gradient(circle at 55% 60%,#f6b24a,#a0521c 40%,#2c2622 75%)"></div>
  <div class="num abs" style="left:186px;top:703px">4</div>
  <div class="caption abs" style="left:74px;top:732px">We then pour the metals into a mold according to the amount of gold that was brought in</div>

  <div class="photo abs" role="img" aria-label="Cooled gold bar out of the mold" style="left:275px;top:631px;background:radial-gradient(circle at 45% 55%,#c9a64a,#6a645c 40%,#8a8682 80%)"></div>
  <div class="caption abs" style="left:260px;top:732px">After the bar cools we then take it out of the mold</div>

  <div class="photo abs" role="img" aria-label="Drilling samples from the bar" style="left:459px;top:631px;background:linear-gradient(135deg,#d8d6d2,#8d8b88 50%,#bdbab5)"></div>
  <div class="num abs" style="left:556px;top:703px">5</div>
  <div class="caption abs" style="left:444px;top:732px">We then drill samples of the bar This is used to test the purity of the metals. This test is done by our State of the Art assaying equipment.</div>
</section>

<section class="step-three">
  <div class="band-gold abs" style="top:852px;height:245px"></div>
  <div class="step-label abs" style="top:814px;left:234px;width:212px">
    <svg width="212" height="50"><polygon points="2,0 210,0 206,36 6,36" fill="#2d2b29"/><polygon points="90,36 122,36 106,50" fill="#f4f4f4"/><polygon points="96,36 116,36 106,44" fill="#2d2b29"/></svg>
    <span class="tight">Step Three - Assaying and Invoicing</span>
  </div>
  <div class="photo abs" role="img" aria-label="Assaying machine" style="left:105px;top:888px;background:linear-gradient(135deg,#e4e2de,#6c7488 55%,#b8b6b2)"></div>
  <div class="photo abs" role="img" aria-label="Spectrometer used for testing" style="left:257px;top:888px;background:linear-gradient(135deg,#2a3a6a,#3c5290 50%,#c6c8cc)"></div>
  <div class="caption lead abs" style="left:110px;top:987px;width:272px;font-size:11.5px;line-height:14px">After drilling a sample from the bar. We will then take the samples and insert them into these machines. Which will give us extremely accurate results.</div>
  <div class="photo abs" role="img" aria-label="Customer paid out at the window" style="left:459px;top:888px;background:linear-gradient(135deg,#a2484a,#c8bfb4 55%,#6a8a9a)"></div>
  <div class="caption lead abs" style="left:444px;top:987px;font-size:11.5px;line-height:14px">After our tests are finished we then write up the invoice and pay out the customer by Cash or Check.</div>
</section>

<footer>
  <div class="footer abs"></div>
  <div class="badge wide abs" style="left:188px"></div>
  <div class="badge abs" style="left:292px"></div>
  <div class="badge abs" style="left:342px"></div>
  <div class="badge abs" style="left:396px"></div>
  <div class="badge abs" style="left:451px"></div>
</footer>

<aside class="price-ticker">
  <div class="ticker-bg abs"></div>
  <div class="ticker abs">
    <div class="t-label abs" style="left:14px">Real-time Price</div>
    <div class="t-field abs" style="left:13px;width:88px;text-align:left;padding-left:8px">Gold
      <svg class="abs" style="right:0;top:0" width="17" height="15"><rect width="17" height="15" rx="2" fill="#1c1b1a"/><polyline points="5,6 8.5,9.5 12,6" fill="none" stroke="#f7c325" stroke-width="2"/></svg>
    </div>
    <div class="t-label abs" style="left:116px">Last Update</div>
    <div class="t-field abs" style="left:115px;width:100px">Fri May 31, 3:59 PM CDT</div>
    <div class="t-label abs" style="left:240px">Bid</div>
    <div class="t-field abs" style="left:230px;width:39px">1,387.40</div>
    <div class="t-label abs" style="left:283px">Ask</div>
    <div class="t-field abs" style="left:273px;width:39px">1,388.30</div>
    <div class="t-label abs" style="left:324px">Low</div>
    <div class="t-field abs" style="left:316px;width:39px">0.00</div>
    <div class="t-label abs" style="left:363px">High</div>
    <div class="t-field abs" style="left:353px;width:39px">0.00</div>
    <div class="t-label abs" style="left:406px">Change</div>
    <div class="t-field change abs" style="left:405px;width:71px">-25.77 (-1.82%)</div>
    <svg class="abs" style="left:490px;top:6px" width="40" height="38" aria-label="Refresh">
      <rect width="40" height="38" rx="3" fill="#1a1918"/>
      <path d="M12 19a8 8 0 0 1 14-5.3" fill="none" stroke="#f7c325" stroke-width="3"/>
      <polygon points="24,9 30,15 23,16" fill="#f7c325"/>
      <path d="M28 19a8 8 0 0 1-14 5.3" fill="none" stroke="#f7c325" stroke-width="3"/>
      <polygon points="16,29 10,23 17,22" fill="#f7c325"/>
    </svg>
  </div>
</aside>

</body>
</html>
```